creation of business cards for Velmora Sàrl

Velmora S% 26 # 224; rl is a soci% 26 # 233; t% 26 # 233; consultancy that accompanies companies in the development of their business on the market% 26 # 233; Switzerland by providing strategic contacts or market information; and by providing administrative or logistical support. Our consulting skills focus on sectors% 26 # 224; high value added% 26 # 233; e, such as trade in food goods% 26 # 39amp; drinks, fashion% 26amp; lifestyle, products and services for% 26 # 233; s in high-tech industries (pharmaceutical, chemical, m% 26 # 233; pricy 26% 23 #; cision) or sustainable solutions (% 26 # 233; energies renewable, mat% 26 # 233; recyclable materials). As part of the launch of our activity% 26 # 233;, we need% 26 # 39;% 26 # 233; to establish business cards to d% 26 # 233; work our new customers (Swiss or international).

Target Market(s)

Companies wishing to develop their activity% 26 # 233; s in Switzerland or% 26 # 224; l% 26 # 39;% 26 # 233; abroad (mainly in Europe).

Contact Information for Business Card

Prénom NOM
Velmora Sàrl
Bureau de Lavertin
Rue des Tilleuls 14, 2000 Neuchâtel
Tél. : 032 718 46 39
info@velmora-conseil.ch
www.velmora-conseil.ch

Font styles to use
Serif
Sans Serif

Colors

Designer to choose colors to be used in the design.

Requirements
Must have
• The logo The name of the company% 26 # 233; t% 26 # 233; (Velmora S% 26 # 224; rl) One field for the mailing address One field for the number% 26 # 233; ro de t% 26 # 233; l% 26 # 233; phone One field for the % 26 # 39; email address and website

```html
<!DOCTYPE html>
<html lang="fr">
<head>
<meta charset="utf-8">
<title>Velmora Sàrl – Cartes de visite</title>
<link rel="stylesheet" href="https://fonts.googleapis.com/css2?family=Lato:wght@300;400;700;900&display=swap">
<style>
  :root {
    --backdrop: #2b2b2d;
    --brand-teal: #02405a;
    --ink-teal: #0d3b52;
    --ink-grey: #4a4f55;
    --rule-teal: #7fa3b2;
    --paper: #ffffff;
    --mark-tint: #dfe5e9;
    --corner-grey: #8a8d90;
  }
  * { box-sizing: border-box; margin: 0; padding: 0; }
  html, body { width: 1200px; height: 878px; overflow: hidden; }
  body {
    background: var(--backdrop);
    font-family: "Lato", Arial, sans-serif;
    position: relative;
  }
  .card {
    position: absolute;
    left: 270px;
    width: 660px;
    height: 377px;
    box-shadow: 0 10px 30px rgba(0,0,0,.45);
    overflow: hidden;
  }

  /* Front */
  .card-front {
    top: 40px;
    background: var(--brand-teal);
    display: flex;
    align-items: center;
    justify-content: center;
    gap: 26px;
  }
  .card-front .brand-square {
    width: 58px;
    height: 58px;
    background: var(--paper);
    border-radius: 12px;
  }
  .card-front .brand-name {
    color: var(--paper);
    font-weight: 300;
    font-size: 56px;
    letter-spacing: 6px;
  }

  /* Back */
  .card-back {
    top: 461px;
    background: var(--paper);
  }
  .company {
    position: absolute;
    left: 40px;
    top: 26px;
  }
  .company-name {
    color: var(--ink-teal);
    font-weight: 900;
    font-size: 30px;
    line-height: 1.1;
  }
  .company-office {
    color: var(--ink-grey);
    font-size: 18px;
    margin-top: 2px;
  }
  .faint-square {
    position: absolute;
    right: 60px;
    top: 80px;
    width: 180px;
    height: 180px;
    background: var(--mark-tint);
    border-radius: 30px;
  }
  .contacts {
    position: absolute;
    left: 40px;
    top: 180px;
    list-style: none;
  }
  .contacts li {
    display: flex;
    align-items: center;
    gap: 14px;
    color: var(--ink-grey);
    font-size: 19px;
    line-height: 29px;
  }
  .contacts svg { width: 17px; height: 17px; fill: var(--ink-teal); flex: none; }
  .contacts .web-domain { color: var(--ink-teal); }
  .divider {
    position: absolute;
    left: 40px;
    right: 60px;
    top: 280px;
    height: 1px;
    background: var(--rule-teal);
  }
  .address {
    position: absolute;
    left: 40px;
    top: 290px;
    display: flex;
    align-items: center;
    gap: 14px;
    color: var(--ink-grey);
    font-size: 19px;
  }
  .address svg { width: 16px; height: 18px; fill: var(--ink-teal); flex: none; }
  .footer-band {
    position: absolute;
    left: 0;
    right: 0;
    bottom: 0;
    height: 18px;
    background: var(--brand-teal);
  }
  .footer-corner {
    position: absolute;
    left: 0;
    bottom: 0;
    width: 40px;
    height: 18px;
    background: var(--corner-grey);
    border-right: 5px solid var(--paper);
  }
</style>
</head>
<body>

<section class="card card-front">
  <div class="brand-square"></div>
  <div class="brand-name">VELMORA</div>
</section>

<section class="card card-back">
  <div class="company">
    <div class="company-name">Velmora Sàrl</div>
    <div class="company-office">Bureau de Lavertin</div>
  </div>

  <div class="faint-square"></div>

  <ul class="contacts">
    <li>
      <svg viewBox="0 0 24 24"><path d="M6.6 10.8a15.1 15.1 0 0 0 6.6 6.6l2.2-2.2a1 1 0 0 1 1-.25 11.4 11.4 0 0 0 3.6.57 1 1 0 0 1 1 1V20a1 1 0 0 1-1 1A17 17 0 0 1 3 4a1 1 0 0 1 1-1h3.5a1 1 0 0 1 1 1c0 1.25.2 2.45.57 3.57a1 1 0 0 1-.25 1z"/></svg>
      <span>032 718 46 39</span>
    </li>
    <li>
      <svg viewBox="0 0 24 24"><path d="M2 5h20v14H2z M2 5l10 8 10-8" stroke="#fff" stroke-width="1.5"/></svg>
      <span>info@velmora-conseil.ch</span>
    </li>
    <li>
      <svg viewBox="0 0 24 24"><circle cx="12" cy="12" r="10"/><path d="M2 12h20M12 2c3 3 3 17 0 20M12 2c-3 3-3 17 0 20" stroke="#fff" stroke-width="1.2" fill="none"/></svg>
      <span>www.<span class="web-domain">velmora-conseil</span>.ch</span>
    </li>
  </ul>

  <div class="divider"></div>

  <div class="address">
    <svg viewBox="0 0 24 28"><path d="M12 0a10 10 0 0 0-10 10c0 7.5 10 18 10 18s10-10.5 10-18A10 10 0 0 0 12 0zm0 14a4 4 0 1 1 0-8 4 4 0 0 1 0 8z"/></svg>
    <span>Rue des Tilleuls 14, 2074 Lavertin</span>
  </div>

  <div class="footer-band"></div>
  <div class="footer-corner"></div>
</section>

</body>
</html>
```